Billboard design - consider what a billboard is

Design a billboard using my logo - Billboard is 6m x 3m
A Billboard is advertising for my company that is on a big sign.

Has to be clean and easy to read, and ideally highlights that we are Residential and Commercial builders.

Keep it clean and easy to read

The contact number for the board is

027 584 9071
www.fernridgebuildworks.co.nz
info@fernridgebuildworks.co.nz

Doesnt have to have all contact details if it doesnt fit

Has to catch peoples attention to contact us if they need a builder

Can you please change the sign to be all white writing, with black background ?
Updates

Please consider what a billboard is...

The design needs to be suitable for a billboard..

Target Market(s)

people driving past

Industry/Entity Type

Construction

Logo Text

Wellington Builder, website email address, contact number

Colors
0054AA
0677BA
7BADD7
CADEEF
E8F1F8

Requirements
Must have
• Easy to read
Nice to have
• easy to read, can clearly see contact details

```html
<!DOCTYPE html>
<html lang="en">
<head>
<meta charset="utf-8">
<title>Fernridge Buildworks Billboard</title>
<link rel="stylesheet" href="https://fonts.googleapis.com/css2?family=Archivo:wdth,wght@125,800;125,900&family=Roboto:wght@700&display=swap">
<style>
  :root {
    --brand-blue: #5b89c6;
    --stone-grey: #726766;
    --board-white: #ffffff;
    --backdrop: #e8f1f8;
  }
  * { margin: 0; padding: 0; box-sizing: border-box; }
  html, body {
    width: 1200px;
    height: 480px;
    overflow: hidden;
    background: var(--backdrop);
  }
  .billboard {
    position: absolute;
    left: 120px;
    top: 0;
    width: 960px;
    height: 480px;
    background: var(--board-white);
    overflow: hidden;
  }
  .brand-name {
    position: absolute;
    left: 58px;
    top: 92px;
    color: var(--brand-blue);
    font-family: "Roboto", Arial, sans-serif;
    font-weight: 700;
    font-size: 76px;
    line-height: 0.98;
    letter-spacing: -1px;
  }
  .services-heading {
    position: absolute;
    left: 602px;
    top: 50px;
    color: var(--brand-blue);
    font-family: "Roboto", Arial, sans-serif;
    font-weight: 700;
    font-size: 39px;
    line-height: 1;
  }
  .service-list {
    position: absolute;
    left: 602px;
    top: 118px;
    list-style: none;
  }
  .service-item {
    position: relative;
    padding-left: 52px;
    margin-bottom: 18px;
    color: var(--stone-grey);
    font-family: "Archivo", "Arial Black", sans-serif;
    font-weight: 900;
    font-stretch: 125%;
    font-size: 26px;
    line-height: 29px;
    letter-spacing: 0.5px;
  }
  .service-marker {
    position: absolute;
    left: 6px;
    top: 2px;
    width: 17px;
    height: 29px;
  }
  .phone-band {
    position: absolute;
    left: 0;
    top: 322px;
    width: 960px;
    height: 85px;
    background: var(--stone-grey);
    display: flex;
    align-items: center;
    justify-content: center;
  }
  .phone-number {
    color: var(--board-white);
    font-family: "Archivo", "Arial Black", sans-serif;
    font-weight: 900;
    font-stretch: 125%;
    font-size: 76px;
    line-height: 1;
    letter-spacing: 2px;
    word-spacing: 14px;
  }
  .website {
    position: absolute;
    left: 0;
    top: 410px;
    width: 960px;
    text-align: center;
    color: var(--brand-blue);
    font-family: "Roboto", Arial, sans-serif;
    font-weight: 700;
    font-size: 50px;
    line-height: 60px;
  }
</style>
</head>
<body>
  <main class="billboard">
    <div class="brand-name">Fernridge<br>Buildworks</div>

    <h2 class="services-heading">SPECIALISING IN</h2>
    <ul class="service-list">
      <li class="service-item">
        <svg class="service-marker" viewBox="0 0 17 29" aria-hidden="true"><polygon points="0,8 17,0 17,21 0,29" fill="var(--stone-grey)"/></svg>
        RESIDENTIAL<br>RENOVATIONS
      </li>
      <li class="service-item">
        <svg class="service-marker" viewBox="0 0 17 29" aria-hidden="true"><polygon points="0,8 17,0 17,21 0,29" fill="var(--brand-blue)"/></svg>
        RESIDENTIAL<br>ALTERATIONS
      </li>
      <li class="service-item">
        <svg class="service-marker" viewBox="0 0 17 29" aria-hidden="true"><polygon points="0,8 17,0 17,21 0,29" fill="var(--stone-grey)"/></svg>
        COMMERCIAL
      </li>
    </ul>

    <div class="phone-band">
      <span class="phone-number">027 584 9071</span>
    </div>

    <div class="website">www.fernridgebuildworks.co.nz</div>
  </main>
</body>
</html>
```